MIRA VANE coconut based Haircare range

I need a label design for my new range of coconut based hair care called Mira Vane.

Mira represents coconut and Vane represents sun.

The label is on a white bottle, so the label you design could be fun and vibrant to represent the brand name.

Tagline: Healthy Happy Hair

The Mira Vane logo needs to be part of this label and hasn't been developed, so feel free to include your design as part of the label.

The winner of this contest will be hired to design additional labels for the other products in the range which includes shampoo, conditioner, hair serum, body lotion, shower gel and massage oil.

Please work on a white pump bottle for shampoo and conditioner for this brief. We do need a theme that will work across all the products in the range.

THE LABEL DIMENSION (WRAP AROUND) 15CM X 11CM
Have fun with this design!

What I am trying to do is get people to envisage that by using this brand they are reminded of GOOD TIMES – HOLIDAYS, FUN, and SUN. Remind them of PARADISE.

We want them to look at the brand and want to buy it because it makes them FEEL GOOD.

This range of luscious, nature based hair products is suitable for every hair type and comes in six refreshing aromas, made with a range of active ingredients including 100% cold-pressed, organic coconut oil.

Thank you for your work!

Target Market(s)

Unisex - people that like fun and natural products

Industry/Entity Type

Hair And Beauty

Colors
0355a3
6b449b
00a990
33a6d7
33b8a4
a6cf38
886aae
a64599

Requirements
Must have
• Vibrant
• Fun
• Logo must work across all products
• Hip
• You can use the words in the file as inspiration or feel free to use the words on the bottle to cultivate a feeling of holidays and this shampoo reminding them of the fun they had.
Nice to have
• A label that can work across different products by changing the colour palette not the whole design
Should not have
• Be too sterile / cold

```html
<!DOCTYPE html>
<html lang="en">
<head>
<meta charset="utf-8">
<title>Mira Vane Nourishing Shampoo Label</title>
<link rel="stylesheet" href="https://fonts.googleapis.com/css2?family=Alex+Brush&family=Josefin+Sans:wght@300;700&family=Oswald:wght@400&display=swap">
<style>
  :root {
    --label-white: #ffffff;
    --sun-orange: #ff3c0a;
    --splash-gold: #f7b733;
    --splash-coral: #f2604a;
    --splash-pink: #ef7f86;
    --text-white: #ffffff;
  }
  * { margin: 0; padding: 0; box-sizing: border-box; }
  html, body {
    width: 1200px;
    height: 893px;
    overflow: hidden;
    background: var(--label-white);
  }
  .label {
    position: relative;
    width: 1200px;
    height: 893px;
    background: var(--label-white);
    overflow: hidden;
  }
  .splash {
    position: absolute;
    left: 40px;
    top: 160px;
    width: 1100px;
    height: 630px;
  }
  .brand-mark {
    position: absolute;
    left: 540px;
    top: 79px;
    width: 120px;
    height: 120px;
    border-radius: 50%;
    background: var(--sun-orange);
    display: flex;
    align-items: center;
    justify-content: center;
  }
  .brand-name {
    font-family: "Josefin Sans", sans-serif;
    font-weight: 700;
    font-size: 19px;
    letter-spacing: 2px;
    color: var(--text-white);
    text-align: center;
    line-height: 1.1;
  }
  .tagline {
    position: absolute;
    left: 500px;
    top: 215px;
    width: 360px;
    font-family: "Alex Brush", cursive;
    color: var(--text-white);
    text-shadow: 2px 3px 5px rgba(120, 40, 20, 0.35);
    line-height: 0.82;
    text-align: center;
  }
  .tagline span { display: block; font-size: 118px; }
  .tagline .line-one { margin-left: 40px; }
  .tagline .line-two { margin-left: 20px; }
  .tagline .line-three { margin-left: -30px; }
  .product-band {
    position: absolute;
    left: 0;
    top: 501px;
    width: 1200px;
    height: 185px;
    background: var(--sun-orange);
  }
  .product-info {
    position: absolute;
    left: 478px;
    top: 20px;
    color: var(--text-white);
  }
  .product-benefit {
    font-family: "Josefin Sans", sans-serif;
    font-weight: 300;
    font-size: 29px;
    letter-spacing: 2.5px;
  }
  .product-type {
    font-family: "Josefin Sans", sans-serif;
    font-weight: 700;
    font-size: 42px;
    letter-spacing: 3px;
    margin-top: 2px;
  }
  .product-rule {
    width: 363px;
    height: 2px;
    background: var(--text-white);
    margin-top: 8px;
  }
  .product-notes {
    font-family: "Oswald", sans-serif;
    font-size: 15px;
    letter-spacing: 0.6px;
    line-height: 22px;
    margin-top: 12px;
  }
  .volume {
    position: absolute;
    left: 0;
    width: 1200px;
    top: 810px;
    text-align: center;
    font-family: "Oswald", sans-serif;
    font-size: 16px;
    letter-spacing: 0.8px;
    color: var(--sun-orange);
  }
</style>
</head>
<body>
  <main class="label">
    <svg class="splash" viewBox="0 0 1100 630" role="img" aria-label="Watercolour splash in warm gold, coral and pink tones">
      <defs>
        <radialGradient id="splash-tone" cx="50%" cy="45%" r="55%">
          <stop offset="0%" stop-color="var(--splash-coral)" stop-opacity="0.9"/>
          <stop offset="45%" stop-color="var(--splash-pink)" stop-opacity="0.75"/>
          <stop offset="75%" stop-color="var(--splash-gold)" stop-opacity="0.6"/>
          <stop offset="100%" stop-color="var(--splash-gold)" stop-opacity="0"/>
        </radialGradient>
      </defs>
      <ellipse cx="560" cy="300" rx="540" ry="300" fill="url(#splash-tone)"/>
    </svg>

    <div class="brand-mark">
      <p class="brand-name">MIRA<br>VANE</p>
    </div>

    <h1 class="tagline">
      <span class="line-one">Healthy</span>
      <span class="line-two">happy</span>
      <span class="line-three">Hair</span>
    </h1>

    <section class="product-band">
      <div class="product-info">
        <p class="product-benefit">NOURISHING</p>
        <h2 class="product-type">SHAMPOO</h2>
        <div class="product-rule"></div>
        <p class="product-notes">MADE WITH ORGANIC COCONUT OIL<br>FOR NORMAL TO DRY HAIR</p>
      </div>
    </section>

    <p class="volume">12 FL. OZ. (355ML)</p>
  </main>
</body>
</html>
```